One-Page Flat Design for SEO Company [2 DAYS]

We need a one-page flat design for our SEO company. Our current website is http://www.rankloft.com/. We are looking to completely re-design the site using new flat design techniques.
Below are some examples of the type of style we're going after:
http://quormel.com/
http://tobyrand.co.uk/
https://pentaly.co/
http://milesporter.me/
As you can see- flat, clean, minimal. It is very important you follow this type of style.
For colour scheme, you may use one of the pre-made colour palettes from here:
http://www.vornacle.com/blog/inspiration/24-flat-designs-with-compelling-color-palettes
I've attached a wireframe to be followed.
Hi,

```html
<!DOCTYPE html>
<html lang="en">
<head>
<meta charset="utf-8">
<title>Rankloft — SEO Packages</title>
<link href="https://fonts.googleapis.com/css2?family=Open+Sans:wght@400;600;700&display=swap" rel="stylesheet">
<style>
:root{
  --orange:#f58a00;
  --mint:#5ef0d6;
  --mint-dark:#1f9c84;
  --mint-button:#177a66;
  --sky:#03c6fb;
  --navy-text:#19486b;
  --price-blue:#1c90e2;
  --card-foot:#0b7fc2;
  --footer:#25282d;
  --footer-bar:#111214;
  --link-blue:#22a3e6;
  --ink:#333;
  --grey-line:#c8c8c8;
  --white:#fff;
}
*{margin:0;padding:0;box-sizing:border-box}
html,body{width:1200px;height:2446px;overflow:hidden}
body{font-family:"Open Sans",Arial,sans-serif;color:var(--ink);background:var(--white);position:relative}
h2,h3,h4{font-weight:400}

/* header */
.site-header{position:absolute;left:0;top:0;width:1200px;height:135px;background:var(--white);border-top:6px solid #2c93d3}
.brand{position:absolute;left:168px;top:26px;display:flex;align-items:center;gap:12px}
.brand-mark{width:30px;height:30px;background:var(--orange);border-radius:50%}
.brand-name{font-size:40px;font-weight:700;color:var(--orange);line-height:1}
.brand-tagline{position:absolute;left:212px;top:72px;font-size:10px;letter-spacing:1px;color:#aaa;text-transform:uppercase}
.main-nav{position:absolute;left:557px;top:36px;display:flex}
.main-nav a{display:block;height:44px;line-height:44px;padding:0 20px;font-size:13px;color:#333;text-decoration:none;text-transform:uppercase}
.main-nav a.active{background:var(--orange);color:var(--white);padding:0 22px;margin-right:8px}

/* hero */
.hero{position:absolute;left:0;top:135px;width:1200px;height:387px;background:var(--mint);border-bottom:4px solid #2a9b86}
.hero-visual{position:absolute;left:215px;top:60px;width:290px;height:290px;border-radius:50%;background:radial-gradient(circle,#9af7e6 0%,#86f4e0 70%,#79f2dc 100%)}
.hero-arrow{position:absolute;top:155px}
.hero-title{position:absolute;left:582px;top:78px;width:433px;height:62px;background:var(--mint-dark);color:var(--white);font-size:29px;line-height:62px;padding-left:18px}
.hero-text{position:absolute;left:582px;top:153px;width:420px;font-size:24px;line-height:33px;color:#16836c}
.hero-button{position:absolute;left:583px;top:269px;width:163px;height:52px;background:var(--mint-button);color:var(--white);font-size:17px;line-height:52px;text-align:center;border-radius:3px}

/* features */
.features{position:absolute;left:0;top:526px;width:1200px;height:457px;background:var(--white)}
.feature{position:absolute;top:36px;width:277px;text-align:center}
.feature-icon{width:132px;height:132px;border-radius:50%;margin:0 auto;border:2px solid #d8d8d8;display:flex;align-items:center;justify-content:center;background:var(--white)}
.feature-icon.filled{background:var(--orange);border-color:var(--orange)}
.feature-title{margin-top:30px;font-size:19px;color:var(--orange);text-transform:uppercase}
.feature-text{margin:16px auto 0;width:266px;font-size:13px;line-height:20px;color:#222}
.feature-more{margin-top:26px;font-size:13px;color:#222}
.feature-rule{margin-top:28px;height:2px;background:var(--grey-line)}
.feature-rule.active{background:#c9a520}

/* packages */
.packages{position:absolute;left:0;top:983px;width:1200px;height:754px;background:var(--sky)}
.packages-title{position:absolute;left:0;top:34px;width:1200px;text-align:center;font-size:40px;color:var(--navy-text);letter-spacing:1px}
.packages-rule{position:absolute;left:508px;top:89px;width:184px;height:1px;background:#6fd9ff}
.packages-intro{position:absolute;left:290px;top:106px;width:620px;text-align:center;font-size:12px;line-height:20px;color:var(--white)}
.plan{position:absolute;top:183px;width:203px;height:514px;background:var(--white)}
.plan-name{height:58px;background:var(--orange);color:var(--white);font-size:22px;line-height:58px;text-align:center;text-transform:uppercase}
.plan-price{height:107px;text-align:center;font-size:56px;line-height:104px;color:var(--price-blue)}
.plan-price sup{font-size:40px;vertical-align:-2px}
.plan-list{list-style:none;font-size:11px;color:#333;text-align:center}
.plan-list li{height:41px;line-height:41px}
.plan-list li.boxed{border-top:1px solid #666;border-bottom:1px solid #666}
.plan-foot{position:absolute;left:0;bottom:0;width:203px;height:118px;background:var(--card-foot);color:var(--white);font-size:14px;line-height:22px;text-align:center;padding-top:26px}

/* testimonial */
.testimonial{position:absolute;left:0;top:1737px;width:1200px;height:390px;background:var(--orange)}
.avatar{position:absolute;left:527px;top:44px;width:146px;height:146px;border-radius:50%;border:4px solid var(--white);background:radial-gradient(circle at 50% 40%,#8a7460 0%,#4e4a4c 60%,#2d3038 100%)}
.testimonial-name{position:absolute;left:0;top:220px;width:1200px;text-align:center;font-size:24px;font-weight:600;color:var(--white)}
.testimonial-text{position:absolute;left:290px;top:278px;width:620px;text-align:center;font-size:13px;line-height:19px;color:var(--white)}
.dots{position:absolute;left:569px;top:340px;display:flex;gap:5px}
.dots span{width:14px;height:14px;border-radius:50%;background:var(--white)}

/* footer */
.site-footer{position:absolute;left:0;top:2127px;width:1200px;height:269px;background:var(--footer);color:#e6e6e6}
.footer-heading{position:absolute;top:34px;font-size:13px;color:var(--link-blue);text-transform:uppercase}
.quick-links{position:absolute;left:168px;top:75px;list-style:none;font-size:12.5px;line-height:23px}
.blog-post{position:absolute;left:315px;width:210px;font-size:11.5px;line-height:16px}
.blog-meta{display:block;font-size:10px;font-style:italic;margin-top:4px}
.blog-more{position:absolute;left:317px;top:226px;font-size:12px;text-decoration:underline}
.address{position:absolute;left:538px;top:75px;width:150px;font-size:11.5px;line-height:16px}
.contact-line{position:absolute;left:538px;font-size:12px;display:flex;align-items:center;gap:10px}
.map{position:absolute;left:705px;top:81px;width:328px;height:104px;background:linear-gradient(135deg,#d9dccb 0%,#cfd6c2 50%,#dcdccf 100%)}
.footer-bar{position:absolute;left:0;top:2396px;width:1200px;height:50px;background:var(--footer-bar)}
.copyright{position:absolute;left:166px;top:16px;font-size:12px;color:#ddd}
.social{position:absolute;left:878px;top:12px;display:flex;gap:7px}
.social span{width:26px;height:26px;border-radius:50%;background:var(--orange)}
</style>
</head>
<body>

<header class="site-header">
  <div class="brand"><span class="brand-mark"></span><span class="brand-name">Rankloft</span></div>
  <div class="brand-tagline">Rank higher, grow your business</div>
  <nav class="main-nav">
    <a class="active">Home</a><a>About</a><a>Service</a><a>FAQ</a><a>Blog</a><a>Contact</a>
  </nav>
</header>

<section class="hero">
  <div class="hero-visual" role="img" aria-label="Illustration of a globe with stacked documents"></div>
  <svg class="hero-arrow" style="left:150px" width="26" height="76" viewBox="0 0 26 76"><polyline points="24,2 3,38 24,74" fill="none" stroke="#fff" stroke-width="3"/></svg>
  <svg class="hero-arrow" style="left:1030px" width="26" height="76" viewBox="0 0 26 76"><polyline points="2,2 23,38 2,74" fill="none" stroke="#fff" stroke-width="3"/></svg>
  <div class="hero-title">LOREM IPSUM DOLOR SIT</div>
  <p class="hero-text">lorem ipsume dolor sit is lorem ipsume dolor sit dummy text</p>
  <div class="hero-button">VIEW MORE</div>
</section>

<section class="features">
  <div class="feature" style="left:166px">
    <div class="feature-icon filled">
      <svg width="70" height="46" viewBox="0 0 70 46"><rect x="4" y="8" width="56" height="30" rx="3" fill="none" stroke="#fff" stroke-width="4" transform="rotate(-12 32 23)"/><circle cx="33" cy="22" r="7" fill="#fff"/></svg>
    </div>
    <h3 class="feature-title">Low Price</h3>
    <p class="feature-text">Lorem Ipsum is simply dummy text of the printing and typesetting industry. Lorem Ipsum has been the industry's standard</p>
    <p class="feature-more">[ Read More ]</p>
    <div class="feature-rule active"></div>
  </div>
  <div class="feature" style="left:461px">
    <div class="feature-icon">
      <svg width="56" height="50" viewBox="0 0 56 50"><rect x="6" y="20" width="8" height="26" fill="#f58a00"/><rect x="18" y="6" width="8" height="40" fill="#f58a00"/><rect x="30" y="26" width="8" height="20" fill="#f58a00"/><rect x="42" y="34" width="8" height="12" fill="#f58a00"/><rect x="2" y="46" width="52" height="3" fill="#f58a00"/></svg>
    </div>
    <h3 class="feature-title">Increase Ranking</h3>
    <p class="feature-text">Lorem Ipsum is simply dummy text of the printing and typesetting industry. Lorem Ipsum has been the industry's standard</p>
    <p class="feature-more">[ Read More ]</p>
    <div class="feature-rule"></div>
  </div>
  <div class="feature" style="left:756px">
    <div class="feature-icon">
      <svg width="70" height="44" viewBox="0 0 70 44"><path d="M4 10 L22 6 L36 16 L50 6 L66 10 L66 26 L50 30 L38 40 L30 40 L16 28 L4 26 Z" fill="#f58a00"/></svg>
    </div>
    <h3 class="feature-title">Quality Service</h3>
    <p class="feature-text">Lorem Ipsum is simply dummy text of the printing and typesetting industry. Lorem Ipsum has been the industry's standard</p>
    <p class="feature-more">[ Read More ]</p>
    <div class="feature-rule"></div>
  </div>
</section>

<section class="packages">
  <h2 class="packages-title">RANKLOFT PACKAGES</h2>
  <div class="packages-rule"></div>
  <p class="packages-intro">Lorem ipsum dolor sit amet, consectetur adipiscing elit. Proin at nunc urna. Pellentesque congue enim sit amet arcu volutpat, quis viverra velit mattis. Vestibulum vel tortor.</p>

  <div class="plan" style="left:166px">
    <div class="plan-name">Bronze</div>
    <div class="plan-price"><sup>$</sup>100</div>
    <ul class="plan-list"><li>10 PR3 - PR8 Social Bookmarks</li><li>15 PR5 - PR8 2.0 Profile Backlinks</li><li class="boxed">100 .EDU Backlinks</li><li>150 PR5 - PR7 Backlinks</li><li>100 Social Bookmarks</li></ul>
    <div class="plan-foot">One Way Links<br>Delivered within 8 days<br>Detailed Submission Report</div>
  </div>
  <div class="plan" style="left:388px">
    <div class="plan-name">Silver</div>
    <div class="plan-price"><sup>$</sup>150</div>
    <ul class="plan-list"><li>10 PR3 - PR8 Social Bookmarks</li><li>15 PR5 - PR8 2.0 Profile Backlinks</li><li class="boxed">100 .EDU Backlinks</li><li>150 PR5 - PR7 Backlinks</li><li>100 Social Bookmarks</li></ul>
    <div class="plan-foot">One Way Links<br>Delivered within 8 days<br>Detailed Submission Report</div>
  </div>
  <div class="plan" style="left:610px">
    <div class="plan-name">Gold</div>
    <div class="plan-price"><sup>$</sup>200</div>
    <ul class="plan-list"><li>10 PR3 - PR8 Social Bookmarks</li><li>15 PR5 - PR8 2.0 Profile Backlinks</li><li class="boxed">100 .EDU Backlinks</li><li>150 PR5 - PR7 Backlinks</li><li>100 Social Bookmarks</li></ul>
    <div class="plan-foot">One Way Links<br>Delivered within 8 days<br>Detailed Submission Report</div>
  </div>
  <div class="plan" style="left:832px">
    <div class="plan-name">Platinum</div>
    <div class="plan-price"><sup>$</sup>300</div>
    <ul class="plan-list"><li>10 PR3 - PR8 Social Bookmarks</li><li>15 PR5 - PR8 2.0 Profile Backlinks</li><li class="boxed">100 .EDU Backlinks</li><li>150 PR5 - PR7 Backlinks</li><li>100 Social Bookmarks</li></ul>
    <div class="plan-foot">One Way Links<br>Delivered within 8 days<br>Detailed Submission Report</div>
  </div>
</section>

<section class="testimonial">
  <div class="avatar" role="img" aria-label="Portrait photo of the client giving the testimonial"></div>
  <h3 class="testimonial-name">DALE THORNE</h3>
  <p class="testimonial-text">Lorem Ipsum is simply dummy text of the printing and typesetting industry. Lorem Ipsum has been the industry's standard dummy text ever since</p>
  <div class="dots"><span></span><span></span><span></span></div>
</section>

<footer class="site-footer">
  <h4 class="footer-heading" style="left:168px">Quick Link</h4>
  <ul class="quick-links"><li>Home</li><li>About us</li><li>Services</li><li>Blog</li><li>Packages</li><li>FAQ</li><li>Contact</li></ul>

  <h4 class="footer-heading" style="left:315px">Blog</h4>
  <div class="blog-post" style="top:75px">Lorem Ipsum has been the industry's standard dummy text<span class="blog-meta">- Nora Vell &nbsp;&nbsp; 15 Dec 2013</span></div>
  <div class="blog-post" style="top:151px">Lorem Ipsum has been the industry's standard dummy text<span class="blog-meta">- Nora Vell &nbsp;&nbsp; 15 Dec 2013</span></div>
  <div class="blog-more">View More</div>

  <h4 class="footer-heading" style="left:540px">Address</h4>
  <p class="address">Lorem Ipsum has been the industry's standard dummy text</p>
  <div class="contact-line" style="top:145px">
    <svg width="14" height="14" viewBox="0 0 14 14"><path d="M3 1 L5 1 L6 4 L4.5 5.5 Q6 8.5 8.5 9.5 L10 8 L13 9 L13 11 Q12 13 10 13 Q1 11 1 3 Q1 1 3 1 Z" fill="#fff"/></svg>555 0142</div>
  <div class="contact-line" style="top:168px">
    <svg width="16" height="12" viewBox="0 0 16 12"><rect x="0.5" y="0.5" width="15" height="11" fill="#fff"/><polyline points="1,1 8,7 15,1" fill="none" stroke="#25282d" stroke-width="1.4"/></svg>hello@rankloft.com</div>

  <div class="map" role="img" aria-label="Map showing the office location"></div>
</footer>

<div class="footer-bar">
  <p class="copyright">Design©2014 . All Rights Reserved</p>
  <div class="social"><span></span><span></span><span></span><span></span><span></span></div>
</div>

</body>
</html>
```